LINGERIE WEBSHOP - Velora casa

We are looking for design and layout design for our webshop. We are company that sells lingerie and other connected textile products liki payamas and etc..
Our website will have approx 500 different products within 2 main catogories Woman/Man) and approx. 10 subcategories
Here is what we expect form design:
-Color pallete should be black and white (if you wish you can add some accent color)
-we want to leave feeling to customers of good quality products towards to luxury
-UX should be simple. Feel free to suggest layout
-frontpage layout, product list layout, product description layout, blog layout
-responsive design, compatible with smartphone

Target Market(s)

woman buying for themself, man buying for woman

Industry/Entity Type

Lingerie

Logo Text

VELORA CASA

Number of Pages Required

4 page

Font styles to use
Sans Serif
Decorative

Requirements
Must have
• simple UX
Nice to have
• difference for sexy/luxury lingerie and daily/cozy lingerie
Should not have
• cheap feel, unreliable

```html
<!DOCTYPE html>
<html lang="en">
<head>
<meta charset="utf-8">
<title>Velora casa — Lingerie Webshop</title>
<link href="https://fonts.googleapis.com/css2?family=Open+Sans:wght@300;400;600;700&family=Playfair+Display:wght@400;700&display=swap" rel="stylesheet">
<style>
:root{
  --ink:#111111;
  --text:#333333;
  --muted:#777777;
  --line:#d8d8d8;
  --paper:#ffffff;
  --footer:#232323;
  --footer-text:#d9d9d9;
  --accent:#d9363e;
}
*{box-sizing:border-box;margin:0;padding:0}
html,body{width:1200px;height:4284px;overflow:hidden;background:var(--paper)}
body{position:relative;font-family:"Open Sans",Arial,sans-serif;color:var(--text)}
.abs{position:absolute}
.serif{font-family:"Playfair Display",Georgia,serif}
.center{text-align:center}
.photo{position:absolute}

/* header */
.site-header{position:absolute;left:0;top:0;width:1200px;height:125px;border-bottom:1px solid var(--line)}
.search{left:110px;top:37px;width:262px;height:43px;border:1px solid #c9c9c9;display:flex;align-items:center;padding-left:14px;font-size:12px;color:#999;gap:6px}
.brand{left:0;width:1200px;top:48px;text-align:center;font-size:44px;font-weight:400;letter-spacing:1px;color:var(--ink);line-height:1}
.icon-btn{width:44px;height:44px;border-radius:50%;border:1px solid #bbb;display:flex;align-items:center;justify-content:center;top:36px}
.icon-btn.dark{background:#3a3a3a;border-color:#3a3a3a}
.main-nav{position:absolute;left:0;top:125px;width:1200px;height:55px;display:flex;justify-content:center;align-items:center;gap:36px;font-family:"Playfair Display",Georgia,serif;font-size:16px;color:#333}
.main-nav .active{text-decoration:underline}
.main-nav .sale{color:var(--accent)}

/* hero */
.hero{left:0;top:180px;width:1200px;height:568px;background:linear-gradient(180deg,#6f9fd3 0%,#9cc3e6 52%,#3f6fa4 56%,#2d5a8c 78%,#1f4670 100%)}
.hero-model{left:700px;top:180px;width:420px;height:568px;background:radial-gradient(ellipse at 50% 55%,#c9926e 0%,#a47054 35%,rgba(40,40,40,.0) 72%)}
.hero-title{left:0;width:722px;top:298px;font-size:74px;color:#fff;text-align:center;line-height:1;font-weight:400}
.hero-sub{left:0;width:722px;top:392px;font-size:45px;color:#fff;text-align:center;line-height:1}
.btn-solid{background:var(--ink);color:#fff;font-weight:700;display:flex;align-items:center;justify-content:center;letter-spacing:.5px}
.btn-line{border:2px solid var(--ink);background:#fff;color:var(--ink);font-weight:700;display:flex;align-items:center;justify-content:center;letter-spacing:.5px}
.arrow{width:30px;height:50px}

/* category */
.cat-card{background:#fff;box-shadow:0 2px 6px rgba(0,0,0,.18);text-align:center}
.cat-title{font-size:46px;font-weight:700;color:var(--ink);margin-top:22px;line-height:1}

/* promo */
.panel{background:#fff;box-shadow:0 2px 6px rgba(0,0,0,.15)}

/* section headings */
.kicker{left:0;width:1200px;text-align:center;font-size:34px;color:#222;line-height:1}
.heading{left:0;width:1200px;text-align:center;font-size:46px;font-weight:700;color:var(--ink);line-height:1}

/* products */
.product-name{font-family:"Playfair Display",Georgia,serif;font-size:22px;color:#333;text-align:center;width:306px}
.product-price{font-size:18px;color:#222;text-align:center;width:306px}

/* blog */
.post-card{background:#fff;box-shadow:0 2px 6px rgba(0,0,0,.15);text-align:center}
.post-title{font-family:"Playfair Display",Georgia,serif;font-size:26px;color:#333;margin-top:26px;line-height:1}
.post-meta{font-size:14px;color:#888;margin-top:14px;display:flex;justify-content:center;align-items:center;gap:6px}
.post-text{font-size:15px;line-height:28px;color:#777;margin-top:8px;padding:0 46px}

/* footer */
.site-footer{left:0;top:3954px;width:1200px;height:330px;background:var(--footer);color:var(--footer-text)}
.footer-brand{left:110px;top:4050px;width:384px;text-align:center;color:#fff;font-size:46px;font-weight:400;line-height:1}
.social{width:40px;height:40px;border-radius:50%;border:1px solid #cfcfcf;top:4123px}
.footer-col h4{font-size:19px;font-weight:400;color:#fff;margin-bottom:12px}
.footer-col a{display:block;font-size:15px;color:var(--footer-text);text-decoration:none;line-height:26.6px}
.rule{left:110px;top:4208px;width:980px;height:1px;background:#555}
.copyright{left:0;width:1200px;top:4233px;text-align:center;font-size:14px;color:#ddd}
</style>
</head>
<body>

<header class="site-header">
  <div class="abs search">
    <svg width="11" height="11" viewBox="0 0 12 12"><circle cx="5" cy="5" r="3.8" fill="none" stroke="#999" stroke-width="1.6"/><line x1="8" y1="8" x2="11" y2="11" stroke="#999" stroke-width="1.8"/></svg>
    SEARCH
  </div>
  <div class="abs brand">VELORA CASA</div>
  <div class="abs icon-btn" style="left:935px">
    <svg width="18" height="16" viewBox="0 0 18 16"><path d="M9 15 L2 8 A4 4 0 0 1 9 3 A4 4 0 0 1 16 8 Z" fill="#888"/></svg>
  </div>
  <div class="abs icon-btn" style="left:988px">
    <svg width="14" height="16" viewBox="0 0 14 16"><circle cx="7" cy="4.5" r="3.5" fill="#888"/><path d="M0 16 Q0 9 7 9 Q14 9 14 16 Z" fill="#888"/></svg>
  </div>
  <div class="abs icon-btn dark" style="left:1042px">
    <svg width="18" height="16" viewBox="0 0 18 16"><path d="M0 1 H3 L5 10 H15 L17 4 H4" fill="none" stroke="#fff" stroke-width="2"/><circle cx="6" cy="13.5" r="1.6" fill="#fff"/><circle cx="14" cy="13.5" r="1.6" fill="#fff"/></svg>
  </div>
</header>

<nav class="main-nav">
  <span class="active">HOME</span><span>LINGERIE</span><span>GIFTS</span><span>BLOG</span><span>COLLECTIONS</span><span>NEW IN</span><span class="sale">SALE!</span>
</nav>

<section>
  <div class="photo hero" role="img" aria-label="Model in black swimsuit by the sea under a blue sky"></div>
  <div class="photo hero-model" role="img" aria-label="Model in black cut-out swimsuit"></div>
  <h1 class="abs serif hero-title">SUMMER SALE</h1>
  <p class="abs serif hero-sub">UP TO 70% OFF</p>
  <a class="abs btn-solid" style="left:234px;top:477px;width:253px;height:66px;font-size:21px">SHOP THE SALE</a>
  <svg class="abs arrow" style="left:42px;top:437px" viewBox="0 0 30 50"><polyline points="24,4 6,25 24,46" fill="none" stroke="#fff" stroke-width="3"/></svg>
  <svg class="abs arrow" style="left:1132px;top:437px" viewBox="0 0 30 50"><polyline points="6,4 24,25 6,46" fill="none" stroke="#fff" stroke-width="3"/></svg>
</section>

<section>
  <div class="photo" style="left:111px;top:818px;width:469px;height:444px;background:linear-gradient(160deg,#cfe9ef 0%,#e9f3f2 45%,#d9b79a 70%,#55c2d6 100%)" role="img" aria-label="Woman in white bikini on a tropical beach"></div>
  <div class="abs cat-card" style="left:203px;top:1197px;width:286px;height:181px">
    <div class="serif cat-title">WOMAN</div>
  </div>
  <a class="abs btn-line" style="left:263px;top:1290px;width:166px;height:55px;font-size:19px">SHOP NOW</a>

  <div class="photo" style="left:618px;top:818px;width:471px;height:444px;background:linear-gradient(160deg,#e9e6e2 0%,#f5f3f0 50%,#dccbbd 75%,#f2efec 100%)" role="img" aria-label="Model in white lace lingerie and open shirt"></div>
  <div class="abs cat-card" style="left:711px;top:1197px;width:286px;height:181px">
    <div class="serif cat-title">MAN</div>
  </div>
  <a class="abs btn-line" style="left:771px;top:1290px;width:166px;height:55px;font-size:19px">SHOP NOW</a>
</section>

<section>
  <div class="photo" style="left:0;top:1456px;width:876px;height:480px;background:linear-gradient(135deg,#ddd0bd 0%,#cfc0a9 45%,#e4d8c6 100%)" role="img" aria-label="Woman in crochet bralette lying on sand"></div>
  <div class="abs panel center" style="left:665px;top:1541px;width:425px;height:306px">
    <div class="serif" style="font-size:48px;font-weight:700;color:var(--ink);margin-top:60px;line-height:1">UP TO 75% OFF</div>
    <div class="serif" style="font-size:34px;color:#222;margin-top:14px;line-height:1">LUXURY LINGERIE</div>
  </div>
  <a class="abs btn-line" style="left:740px;top:1725px;width:276px;height:57px;font-size:19px">SHOP THE COLLECTION</a>
</section>

<section>
  <p class="abs serif kicker" style="top:2003px">TOP SELLING</p>
  <h2 class="abs serif heading" style="top:2055px">BEST OF THE BASICS</h2>

  <svg class="abs arrow" style="left:42px;top:2302px" viewBox="0 0 30 50"><polyline points="24,4 6,25 24,46" fill="none" stroke="#888" stroke-width="3"/></svg>
  <svg class="abs arrow" style="left:1132px;top:2302px" viewBox="0 0 30 50"><polyline points="6,4 24,25 6,46" fill="none" stroke="#888" stroke-width="3"/></svg>

  <div class="photo" style="left:111px;top:2144px;width:306px;height:364px;background:linear-gradient(180deg,#e6eef2 0%,#d6e3ea 55%,#c89a83 100%)" role="img" aria-label="Model in pink bikini by the sea"></div>
  <svg class="abs" style="left:133px;top:2464px" width="26" height="24" viewBox="0 0 26 24"><path d="M13 22 L3 12 A5.5 5.5 0 0 1 13 5 A5.5 5.5 0 0 1 23 12 Z" fill="none" stroke="#fff" stroke-width="2"/></svg>
  <p class="abs product-name" style="left:111px;top:2527px">Finibus Bonoret Maloru</p>
  <p class="abs product-price" style="left:111px;top:2564px">$150</p>

  <div class="photo" style="left:447px;top:2144px;width:306px;height:364px;background:linear-gradient(180deg,#f4f4f3 0%,#faf9f8 60%,#f0ece8 100%);border:1px solid #e2e2e2" role="img" aria-label="Model in white lingerie, faded on hover"></div>
  <div class="abs" style="left:509px;top:2254px;width:182px;height:60px;border:2px solid #222;background:rgba(255,255,255,.6);display:flex;align-items:center;justify-content:center;gap:28px;font-size:15px;color:#222">
    SELECT SIZE
    <svg width="10" height="7" viewBox="0 0 10 7"><polyline points="1,1 5,5 9,1" fill="none" stroke="#222" stroke-width="1.5"/></svg>
  </div>
  <a class="abs btn-solid" style="left:510px;top:2342px;width:180px;height:56px;font-size:16px">ADD TO CART</a>
  <p class="abs product-name" style="left:447px;top:2527px">Finibus Bonoret Maloru</p>
  <p class="abs product-price" style="left:447px;top:2564px">$150</p>

  <div class="photo" style="left:781px;top:2144px;width:308px;height:364px;background:linear-gradient(160deg,#5b8aa4 0%,#8a7f73 40%,#5a5650 70%,#7b7670 100%)" role="img" aria-label="Model in leopard print bikini on rocks by the sea"></div>
  <svg class="abs" style="left:802px;top:2464px" width="26" height="24" viewBox="0 0 26 24"><path d="M13 22 L3 12 A5.5 5.5 0 0 1 13 5 A5.5 5.5 0 0 1 23 12 Z" fill="none" stroke="#fff" stroke-width="2"/></svg>
  <p class="abs product-name" style="left:781px;top:2527px">Finibus Bonoret Maloru</p>
  <p class="abs product-price" style="left:781px;top:2564px">$150</p>
</section>

<section>
  <div class="photo" style="left:321px;top:2646px;width:879px;height:482px;background:linear-gradient(135deg,#d6e4ec 0%,#9bb6c7 35%,#6c7c86 60%,#4a6d86 100%)" role="img" aria-label="Woman in black bikini reclining on a seaside rock"></div>
  <div class="abs panel center" style="left:110px;top:2731px;width:425px;height:306px">
    <div class="serif" style="font-size:48px;font-weight:700;color:var(--ink);margin-top:28px;line-height:1">GET MORE</div>
    <div class="serif" style="font-size:36px;color:#222;margin-top:12px;line-height:1">LINGERIE LOVE, FIRST.</div>
  </div>
  <div class="abs" style="left:133px;top:2877px;width:381px;height:55px;border:1px solid #ccc;display:flex;align-items:center;padding-left:16px;gap:10px;font-size:15px;color:#888">
    <svg width="16" height="12" viewBox="0 0 16 12"><rect width="16" height="12" fill="#888"/><polyline points="0,0 8,7 16,0" fill="none" stroke="#fff" stroke-width="1.4"/></svg>
    Email Address
  </div>
  <a class="abs btn-solid" style="left:253px;top:2950px;width:139px;height:57px;font-size:19px">SIGN UP</a>
</section>

<section>
  <p class="abs serif kicker" style="top:3195px">FROM THE</p>
  <h2 class="abs serif heading" style="top:3246px">BLOG</h2>

  <div class="photo" style="left:111px;top:3344px;width:469px;height:324px;background:linear-gradient(180deg,#1d5a8c 0%,#2f7aa8 40%,#c2b6a3 62%,#a89a86 100%)" role="img" aria-label="Woman lying on a rocky shore by deep blue water"></div>
  <div class="abs post-card" style="left:145px;top:3613px;width:403px;height:268px">
    <div class="post-title">Finibus Bonoruet Maloru</div>
    <div class="post-meta">
      <svg width="12" height="12" viewBox="0 0 12 12"><rect x="0" y="2" width="12" height="10" fill="#999"/><rect x="2" y="0" width="2" height="3" fill="#999"/><rect x="8" y="0" width="2" height="3" fill="#999"/></svg>
      21/07/2020 &nbsp;|&nbsp;
      <svg width="11" height="12" viewBox="0 0 14 16"><circle cx="7" cy="4.5" r="3.5" fill="#999"/><path d="M0 16 Q0 9 7 9 Q14 9 14 16 Z" fill="#999"/></svg>
      Admin
    </div>
    <p class="post-text">Nemo enim ipsam voluptatem quia volu ptas sit aspernatur aut odit aut fugit, sed quia consequuntur magni dolo</p>
  </div>
  <a class="abs btn-line" style="left:273px;top:3801px;width:146px;height:52px;font-size:16px">READ MORE</a>

  <div class="photo" style="left:618px;top:3344px;width:471px;height:324px;background:linear-gradient(180deg,#2b8fa6 0%,#7a7a72 30%,#8c8a84 65%,#6f6d68 100%)" role="img" aria-label="Woman in black swimsuit lying on a large rock"></div>
  <div class="abs post-card" style="left:652px;top:3613px;width:404px;height:268px">
    <div class="post-title">Finibus Bonoruet Maloru</div>
    <div class="post-meta">
      <svg width="12" height="12" viewBox="0 0 12 12"><rect x="0" y="2" width="12" height="10" fill="#999"/><rect x="2" y="0" width="2" height="3" fill="#999"/><rect x="8" y="0" width="2" height="3" fill="#999"/></svg>
      21/07/2020 &nbsp;|&nbsp;
      <svg width="11" height="12" viewBox="0 0 14 16"><circle cx="7" cy="4.5" r="3.5" fill="#999"/><path d="M0 16 Q0 9 7 9 Q14 9 14 16 Z" fill="#999"/></svg>
      Admin
    </div>
    <p class="post-text">Nemo enim ipsam voluptatem quia volu ptas sit aspernatur aut odit aut fugit, sed quia consequuntur magni dolo</p>
  </div>
  <a class="abs btn-line" style="left:780px;top:3801px;width:148px;height:52px;font-size:16px">READ MORE</a>
</section>

<footer>
  <div class="abs site-footer"></div>
  <div class="abs footer-brand">VELORA CASA</div>
  <span class="abs social" style="left:208px"></span>
  <span class="abs social" style="left:258px"></span>
  <span class="abs social" style="left:309px"></span>
  <span class="abs social" style="left:359px"></span>

  <div class="abs footer-col" style="left:564px;top:3994px">
    <h4>INFORMATION</h4>
    <a>About Us</a><a>Contact Us</a><a>FAQ's</a><a>Size Guides</a><a>Our Blog</a>
  </div>
  <div class="abs footer-col" style="left:778px;top:3994px">
    <h4>QUICK LINKS</h4>
    <a>Delivery &amp; Shipping</a><a>Returns &amp; Exchanges</a><a>Terms &amp; Conditions</a><a>Privacy Policy</a><a>Stores &amp; Stockists</a>
  </div>
  <div class="abs rule"></div>
  <p class="abs copyright">Copyright © 2020 LINGERIE WEBSHOP.</p>
</footer>

</body>
</html>
```